Vela Care is an innovative Australian Business offering organisations an online solution for depre

We need an extremely professional Business card that is positive as we offer engaging online technology to help with depression. Our target market is large scale adoption by major Organisations.The logo is supplied but font can alter .

We would like to see designs that use our logo on the front with altered font . Open to alteration on the sphere concept for the logo but happy with this and you may alter slightly if you wish.

back -displays contact details, with our names coloured in orange like the orange on our site . use creative flair

initial names to appear on cards are Sam Whitfield Director 0432516087 Sa.Whitfieldd@vela-care.com.au, www.vela-care.com.au

We are looking for fresh and professional designs with some creative flair.

i have attached a mock up of our site that should come across in the business card design...but
No images required from site

business card dimensions are 54x89. we will print logo in high gloss and card will be matt.

Target Market(s)

Large adoption by Doctors , Universities , not for profits and large organisations

Industry/Entity Type

Business

Requirements
Must have
• linkage to our site by way of design but no images needed from site except logo

Needs to be bright and vibrant in design as online tools for depression and anxiety . Also professional look.

```html
<!DOCTYPE html>
<html lang="en">
<head>
<meta charset="utf-8">
<title>Vela Care – Business Card</title>
<link href="https://fonts.googleapis.com/css2?family=Jost:wght@400;600&display=swap" rel="stylesheet">
<style>
  :root {
    --backdrop: #3b3b3c;
    --card-front: #e9e7e0;
    --card-back: #353f55;
    --ink-dark: #3a3a3a;
    --ink-light: #d5d8de;
    --accent-orange: #f0961e;
  }
  * { box-sizing: border-box; margin: 0; padding: 0; }
  html, body { width: 1200px; height: 900px; overflow: hidden; }
  body {
    background: var(--backdrop);
    font-family: "Jost", "Century Gothic", sans-serif;
    display: flex;
    align-items: center;
    justify-content: center;
    gap: 40px;
  }
  .card {
    position: relative;
    width: 540px;
    height: 328px;
    border-radius: 2px;
    box-shadow: 0 10px 30px rgba(0,0,0,.35);
  }
  .card--front { background: var(--card-front); }
  .card--back { background: var(--card-back); }

  .brand {
    position: absolute;
    font-size: 40px;
    font-weight: 400;
    letter-spacing: .5px;
    line-height: 1;
    white-space: nowrap;
  }
  .card--front .brand { left: 50%; top: 50%; transform: translate(-50%, -50%); color: var(--ink-dark); }
  .card--back .brand { left: 38px; top: 98px; color: var(--ink-light); }

  .tagline {
    position: absolute; left: 232px; top: 150px;
    font-size: 12px; color: var(--accent-orange); letter-spacing: .3px;
    white-space: nowrap;
  }

  .person { position: absolute; left: 38px; bottom: 36px; }
  .person__name { font-size: 17px; font-weight: 600; color: var(--accent-orange); letter-spacing: .6px; text-transform: uppercase; line-height: 1.1; white-space: nowrap; }
  .person__role { font-size: 13px; color: var(--ink-light); }

  .contacts { position: absolute; display: flex; flex-direction: column; gap: 6px; }
  .contacts--phones { left: 232px; bottom: 56px; }
  .contacts--online { left: 360px; bottom: 56px; }
  .contact { display: flex; align-items: center; gap: 7px; font-size: 12px; color: var(--ink-light); white-space: nowrap; }
  .contact__icon { width: 12px; height: 12px; flex: none; }
</style>
</head>
<body>
  <section class="card card--front" aria-label="Card front">
    <p class="brand">Vela Care</p>
  </section>

  <section class="card card--back" aria-label="Card back">
    <p class="brand">Vela Care</p>
    <p class="tagline">Mental Health And Wellbeing</p>

    <div class="person">
      <p class="person__name">Sam Whitfield</p>
      <p class="person__role">Director</p>
    </div>

    <div class="contacts contacts--phones">
      <p class="contact">
        <svg class="contact__icon" viewBox="0 0 12 12" aria-hidden="true"><circle cx="6" cy="6" r="6" fill="var(--accent-orange)"/><path d="M4 3.2c.4 0 .7.9.7 1.2s-.5.4-.4.7c.3.7.8 1.2 1.5 1.5.3.1.4-.4.7-.4s1.2.3 1.2.7-.6 1-1.2 1C4.8 7.9 4.1 6.9 3.2 5.3c0-.9.4-2.1.8-2.1z" fill="var(--card-back)"/></svg>
        0432516087
      </p>
      <p class="contact">
        <svg class="contact__icon" viewBox="0 0 12 12" aria-hidden="true"><circle cx="6" cy="6" r="6" fill="var(--accent-orange)"/><rect x="4.2" y="2.6" width="3.6" height="6.8" rx=".7" fill="var(--card-back)"/></svg>
        0432516087
      </p>
    </div>

    <div class="contacts contacts--online">
      <p class="contact">
        <svg class="contact__icon" viewBox="0 0 12 12" aria-hidden="true"><circle cx="6" cy="6" r="6" fill="var(--accent-orange)"/><rect x="3" y="4" width="6" height="4.2" fill="var(--card-back)"/><path d="M3 4l3 2.4L9 4" stroke="var(--accent-orange)" stroke-width=".7" fill="none"/></svg>
        info@vela-care.com.au
      </p>
      <p class="contact">
        <svg class="contact__icon" viewBox="0 0 12 12" aria-hidden="true"><circle cx="6" cy="6" r="6" fill="var(--accent-orange)"/><circle cx="6" cy="6" r="3" fill="none" stroke="var(--card-back)" stroke-width=".8"/><path d="M3 6h6M6 3c-1.2 1.6-1.2 4.4 0 6M6 3c1.2 1.6 1.2 4.4 0 6" stroke="var(--card-back)" stroke-width=".7" fill="none"/></svg>
        www.vela-care.com.au
      </p>
    </div>
  </section>
</body>
</html>
```